Surface Protection company needs cards

We are a New Zealand company that will apply nanotechnology coatings on surfaces to prevent growth and spread of bacteria, viruses, mold etc with a sprayer. We deal with large corporates, airlines, hospitals and schools so we are after a new modern, simple and clean look that will have great visual impact.
We a company that is focused on prevention and protection.

Company name, Vela Shield

Subtext, Antimicrobial Surface Protection

Logo, VS

Target Market(s)

Hospitals, Transport agencies, Airlines, Corporate entities

Contact Information for Business Card

Company name, VelaShield
Logo, VS

Gareth Tolley
velashieldnz@postbox.example
+64219305562
www.velashield.example.nz

Requirements
Must have
• Simple clean look.
Nice to have
• We apply nano coatings so try and incorporate this into a theme somehow

```html
<!DOCTYPE html>
<html lang="en">
<head>
<meta charset="utf-8">
<title>Vela Shield – Business Cards</title>
<link rel="stylesheet" href="https://fonts.googleapis.com/css2?family=Fira+Sans:wght@700&family=Saira:wght@400&display=swap">
<style>
  :root {
    --page: #e3e5e7;
    --card-dark: #15191d;
    --card-mid: #26303a;
    --orange: #f7871d;
    --red: #e6241b;
    --white: #ffffff;
  }
  * { margin: 0; padding: 0; box-sizing: border-box; }
  html, body { width: 1200px; height: 1200px; overflow: hidden; }
  body { background: var(--page); position: relative; font-family: "Saira", sans-serif; }

  .card {
    position: absolute;
    left: 258px;
    width: 686px;
    height: 420px;
    border-radius: 30px;
    overflow: hidden;
    color: var(--white);
  }
  .card--front { top: 134px; }
  .card--back { top: 644px; }

  .card__texture {
    position: absolute; inset: 0;
    background: radial-gradient(ellipse at 40% 35%, var(--card-mid) 0%, var(--card-dark) 75%);
  }
  .card__art { position: absolute; inset: 0; width: 100%; height: 100%; }

  .brand-name, .tagline, .person, .contact, .website {
    position: absolute; line-height: 1; white-space: nowrap;
  }
  .brand-name { font-family: "Fira Sans", sans-serif; font-weight: 700; transform: translateX(-50%); }
  .tagline { transform: translateX(-50%); letter-spacing: 0.06em; }

  .card--front .brand-name { left: 404px; top: 60px; font-size: 55px; }
  .card--front .tagline { left: 404px; top: 121px; font-size: 17px; }
  .person { left: 98px; top: 243px; font-size: 31px; letter-spacing: 0.06em; }
  .contact--email { left: 94px; top: 313px; font-size: 24px; letter-spacing: 0.02em; }
  .contact--phone { left: 89px; top: 369px; font-size: 31px; letter-spacing: 0.02em; }

  .card--back .brand-name { left: 345px; top: 148px; font-size: 72px; }
  .card--back .tagline { left: 345px; top: 240px; font-size: 22px; }
  .website { left: 345px; top: 378px; font-size: 19px; transform: translateX(-50%); letter-spacing: 0.04em; }
</style>
</head>
<body>

<section class="card card--front">
  <div class="card__texture" role="img" aria-label="Dark surface covered in water droplets, showing a nano-coating bead effect"></div>
  <svg class="card__art" viewBox="0 0 572 350" aria-hidden="true">
    <defs>
      <linearGradient id="band-fill" x1="0" x2="1">
        <stop offset="0" stop-color="#f36a18"/>
        <stop offset="1" stop-color="#f79a22"/>
      </linearGradient>
      <linearGradient id="icon-fill" x1="0" x2="1">
        <stop offset="0" stop-color="#e6241b"/>
        <stop offset="1" stop-color="#f7871d"/>
      </linearGradient>
    </defs>
    <path class="accent-band" d="M388 181 H572 V218 H436 C410 218 405 190 388 181 Z" fill="url(#band-fill)"/>
    <path class="accent-line" d="M0 176 H382 C408 176 412 218 440 218 H572" fill="none" stroke="var(--red)" stroke-width="4"/>
    <path d="M0 181 H380" stroke="var(--orange)" stroke-width="3"/>

    <g class="icon icon--email">
      <circle cx="41" cy="271" r="16" fill="url(#icon-fill)"/>
      <rect x="32" y="264" width="18" height="13" fill="none" stroke="#fff" stroke-width="2"/>
      <path d="M32 264 L41 272 L50 264" fill="none" stroke="#fff" stroke-width="2"/>
    </g>
    <g class="icon icon--phone">
      <circle cx="40" cy="321" r="16" fill="url(#icon-fill)"/>
      <path d="M33 313 c2 -2 4 -1 5 1 l2 3 c1 2 0 3 -1 4 c1 3 3 5 6 6 c1 -1 2 -2 4 -1 l3 2 c2 1 3 3 1 5 c-2 2 -5 3 -9 1 c-5 -3 -9 -7 -11 -12 c-1 -4 -1 -7 0 -9 z" fill="#fff"/>
    </g>
  </svg>
  <h1 class="brand-name">Vela Shield</h1>
  <p class="tagline">Antimicrobial Surface Protection</p>
  <p class="person">Gareth Tolley</p>
  <p class="contact contact--email">velashieldnz@postbox.example</p>
  <p class="contact contact--phone">+64219305562</p>
</section>

<section class="card card--back">
  <div class="card__texture" role="img" aria-label="Dark surface covered in water droplets, showing a nano-coating bead effect"></div>
  <svg class="card__art" viewBox="0 0 572 350" aria-hidden="true">
    <g class="frame-line frame-line--top" fill="none">
      <path d="M0 25 H45 C70 25 70 62 95 62 H480 C505 62 505 25 530 25 H572" stroke="var(--orange)" stroke-width="6"/>
      <path d="M0 20 H45 C70 20 70 57 95 57 H480 C505 57 505 20 530 20 H572" stroke="var(--red)" stroke-width="2.5"/>
    </g>
    <g class="frame-line frame-line--bottom" fill="none">
      <path d="M0 318 H45 C70 318 70 289 95 289 H485 C510 289 510 318 535 318 H572" stroke="var(--orange)" stroke-width="6"/>
      <path d="M0 313 H45 C70 313 70 284 95 284 H485 C510 284 510 313 535 313 H572" stroke="var(--red)" stroke-width="2.5"/>
    </g>
  </svg>
  <h2 class="brand-name">Vela Shield</h2>
  <p class="tagline">Antimicrobial Surface Protection</p>
  <p class="website">www.velashield.example.nz</p>
</section>

</body>
</html>
```